Brightwell Systems - Company Overview Brochure

We would like a single page A4 Brochure to give to new potential customers to provide a quick overview of our company. This will be used in presales meetings.

We have included the content we would like on the brochure under "Brightwell Systems Marketing Brochure.docx".

We have included two other designs "timebundleterms v4.pdf and Brightwell Public Cloud Plans.pdf" which shows similar marketing brochures we have. We would like these designs to have the same Brightwell Blue and "Specialised Technology Consultancy firm" theme.

Target Market(s)

Technology Sector

Industry/Entity Type

Information Technology

Colors
0054AA
0677BA
7BADD7
CADEEF
E8F1F8

Requirements
Must have
• "Innovative Tech Company Theme".

```html
<!DOCTYPE html>
<html lang="en">
<head>
<meta charset="utf-8">
<title>Brightwell Systems – Specialised Consulting</title>
<link rel="stylesheet" href="https://fonts.googleapis.com/css2?family=Bebas+Neue&family=Inter:wght@400;600;700&display=swap">
<style>
  :root{
    --stage:#e3e3e5;
    --navy-deep:#082a74;
    --brand-blue:#0054aa;
    --brand-mid:#0677ba;
    --brand-sky:#7badd7;
    --brand-pale:#cadeef;
    --brand-mist:#e8f1f8;
    --icon-blue:#0a47c0;
    --ink:#2a2b38;
    --black:#000;
    --white:#fff;
    --rule:#3d62c9;
  }
  *{box-sizing:border-box;margin:0;padding:0}
  html,body{width:1200px;height:1137px;overflow:hidden;background:var(--stage)}
  .flyer{position:absolute;left:244px;top:67px;width:717px;height:1016px;overflow:hidden;
    font-family:"Inter",Arial,sans-serif;color:var(--white)}
  .flyer-shapes{position:absolute;inset:0;width:717px;height:1016px}
  .hero-photo{position:absolute;left:244px;top:0;width:473px;height:490px;
    background:
      radial-gradient(ellipse at 70% 35%,rgba(123,173,215,.55),transparent 60%),
      radial-gradient(ellipse at 40% 70%,rgba(6,119,186,.5),transparent 65%),
      linear-gradient(160deg,#1a5fc4,#0a3f9a 70%);
    -webkit-mask-image:linear-gradient(to right,transparent,#000 35%,#000 80%,transparent 100%),linear-gradient(#000 70%,transparent);
    -webkit-mask-composite:source-in;
    mask-image:linear-gradient(to right,transparent,#000 35%);}
  .brand{position:absolute;left:38px;top:84px;display:flex;align-items:center;gap:12px}
  .brand-square{width:34px;height:34px;background:var(--white)}
  .brand-name{font-weight:700;font-size:18px;letter-spacing:.08em;color:var(--white)}
  .tagline{position:absolute;left:38px;top:151px;width:225px;height:30px;
    border-top:2px solid #2f7fe0;border-bottom:2px solid #2f7fe0;
    font-weight:700;font-size:16px;line-height:26px;text-align:center;letter-spacing:.02em}
  .headline{position:absolute;left:36px;top:212px;font-family:"Bebas Neue",Impact,sans-serif;
    font-size:86px;line-height:66px;font-weight:400;letter-spacing:.005em}
  .section-title{position:absolute;font-family:"Bebas Neue",Impact,sans-serif;font-weight:400;font-size:29px;line-height:1}
  .commitment-title{left:38px;top:377px}
  .commitment-sub{position:absolute;left:38px;top:410px;font-weight:600;font-size:14px;color:var(--brand-sky)}
  .body-copy{position:absolute;left:38px;width:322px;font-size:12px;line-height:14.5px;text-align:justify;color:var(--brand-mist)}
  .copy-one{top:441px}
  .copy-two{top:527px}
  .policy-title{left:443px;top:438px}
  .policy-item{position:absolute;left:443px;width:240px}
  .policy-item h3{font-size:13px;font-weight:700;color:var(--brand-sky);line-height:16px}
  .policy-item p{font-size:12px;line-height:14.5px;color:var(--brand-mist)}
  .policy-fair{top:481px}
  .policy-cost{top:556px}
  .band-title{position:absolute;font-family:"Bebas Neue",Impact,sans-serif;font-weight:400;color:var(--white)}
  .it-title{left:38px;top:594px;font-size:28px}
  .security-title{right:33px;top:658px;font-size:21px;line-height:22px;text-align:right}
  .service{position:absolute;font-size:13px;font-weight:700;line-height:15px;color:var(--ink);letter-spacing:.02em;text-transform:uppercase;transform:translateY(-50%)}
  .service-left{left:96px}
  .service-right{right:95px;text-align:right}
  .terms{position:absolute;left:38px;top:936px;width:200px;font-size:11.5px;line-height:14px;color:var(--brand-mist)}
  .terms-url{position:absolute;left:338px;top:983px;font-size:13px;font-weight:600;color:var(--white)}
</style>
</head>
<body>
<article class="flyer">
  <svg class="flyer-shapes" viewBox="0 0 618 875" preserveAspectRatio="none" aria-hidden="true">
    <defs>
      <linearGradient id="panelBlue" x1="0" y1="0" x2="1" y2="1">
        <stop offset="0" stop-color="#08307e"/>
        <stop offset=".6" stop-color="#0a44a6"/>
        <stop offset="1" stop-color="#0b52b8"/>
      </linearGradient>
    </defs>
    <rect class="panel" width="618" height="875" fill="url(#panelBlue)"/>
  </svg>

  <div class="hero-photo" role="img" aria-label="Photo of a consultant viewing glowing data screens over a blue digital network background"></div>

  <svg class="flyer-shapes" viewBox="0 0 618 875" preserveAspectRatio="none" aria-hidden="true">
    <polygon class="services-panel" points="0,554 345,554 415,615 618,615 618,827 280,827 200,767 0,767" fill="#fff"/>
    <polygon class="footer-panel" points="0,767 200,767 280,827 618,827 618,875 0,875" fill="#082a74"/>
    <polygon class="url-bar" points="270,839 618,839 618,875 258,875" fill="#0a4fb0"/>
    <polygon class="it-band" points="0,495 260,495 345,554 0,554" fill="#000"/>
    <polygon class="security-band" points="345,557 618,557 618,615 415,615" fill="#000"/>
    <g class="row-rules" fill="none" stroke="#3d62c9" stroke-width=".9">
      <polyline points="0,606 290,606 380,668 618,668"/>
      <polyline points="0,658 255,658 345,720 618,720"/>
      <polyline points="0,711 220,711 305,773 618,773"/>
    </g>
    <g class="icons" fill="#0a47c0">
      <rect x="33" y="562" width="38" height="38"/>
      <rect x="33" y="614" width="38" height="38"/>
      <rect x="33" y="667" width="38" height="38"/>
      <rect x="33" y="721" width="38" height="38"/>
      <rect x="553" y="625" width="38" height="38"/>
      <rect x="553" y="676" width="38" height="38"/>
      <rect x="553" y="729" width="38" height="38"/>
      <rect x="553" y="782" width="38" height="38"/>
    </g>
    <g class="icon-marks" fill="none" stroke="#fff" stroke-width="1.8" stroke-linecap="round" stroke-linejoin="round">
      <path d="M52 572 l9 9 -9 9 -9 -9z M52 577 v8 M48 581 h8"/>
      <circle cx="49" cy="629" r="3.5"/><path d="M42 642 c0-5 4-8 7-8 s7 3 7 8 M57 625 l3 0 M58.5 623.5 v3"/>
      <path d="M52 675 l8 3 v6 c0 6-4 9-8 11 -4-2-8-5-8-11 v-6z M52 683 v4"/>
      <path d="M48 734 l-5 6 5 6 M56 734 l5 6 -5 6"/>
      <path d="M564 638 l8 -5 10 9 -6 5z M564 634 v10 M576 647 l2 4"/>
      <rect x="566" y="693" width="12" height="10"/><path d="M568 693 v-4 a4 4 0 0 1 8 0 v4 M572 697 v2"/>
      <path d="M566 740 v10 a3 3 0 0 0 6 0 v-6 a3 3 0 0 1 6 0 v10 M566 738 v-3 M578 754 v3"/>
      <path d="M563 797 a13 13 0 0 1 18 0 M566 801 a8 8 0 0 1 12 0 M569 805 a3.5 3.5 0 0 1 6 0"/><circle cx="572" cy="809" r="1" fill="#fff"/>
    </g>
  </svg>

  <div class="brand"><span class="brand-square"></span><span class="brand-name">BRIGHTWELL SYSTEMS</span></div>
  <div class="tagline">SPECIALISED CONSULTING</div>

  <h1 class="headline">Do it once.<br>Do it right.</h1>

  <h2 class="section-title commitment-title">Our Commitment</h2>
  <p class="commitment-sub">Specialised expertise. Tailored outcomes.</p>
  <p class="body-copy copy-one">Brightwell Systems delivers tailored technology consulting services to government and enterprise organisations. Our approach is built on technical excellence, vendor best practices, and a commitment to getting things right the first time.</p>
  <p class="body-copy copy-two">We focus on solutions that reduce risk, minimise rework, &amp; provide long-term value rather than short-term fixes.</p>

  <h2 class="section-title policy-title">Our Policy</h2>
  <div class="policy-item policy-fair">
    <h3>BE FAIR</h3>
    <p>Fair pricing creates sustainable partnerships &amp; allows us to consistently deliver high-quality outcomes.</p>
  </div>
  <div class="policy-item policy-cost">
    <h3>BE COST EFFECTIVE</h3>
    <p>We believe intelligent &amp; efficient consulting can provide exceptional results without unnecessary complexity or expense.</p>
  </div>

  <h2 class="band-title it-title">IT Services</h2>
  <h2 class="band-title security-title">Electronic Security<br>&amp; Communication</h2>

  <p class="service service-left" style="top:672px">Project<br>Integration</p>
  <p class="service service-left" style="top:733px">Managed<br>Service</p>
  <p class="service service-left" style="top:795px">Enterprise<br>Security</p>
  <p class="service service-left" style="top:857px">Software<br>Development</p>

  <p class="service service-right" style="top:747px">CCTV</p>
  <p class="service service-right" style="top:805px">Integrated<br>Electronic Security</p>
  <p class="service service-right" style="top:867px">Structured Cabling<br>and Fibre Optics</p>
  <p class="service service-right" style="top:928px">Wireless<br>Communication</p>

  <p class="terms">All goods and services provided by Brightwell are provided in accordance with our Standard Terms and Conditions available at</p>
  <p class="terms-url">https://www.brightwellsystems.com.au/t&amp;c</p>
</article>
</body>
</html>
```